Meadowlark Counseling Partners, LLC Needs Modern Business Card Design.

We provide behavioral health services from western Kansas to eastern Kansas. There is an abundance of competition for the services we provide with our main competitor being larger and having significantly more financial resources; however, the quality of services we provide is greater and we have started to catch the attention of the State of Kansas. We had a great logo designed by ArtFolio - this will be used to build upon our brand. The logo (attached) should be used in the card development. We want something unique, modern, but also a card design that clearly states our name, contact info, provides the name and unqiue location of each clinician, etc. Rounded edges, or a unique size, just something that makes our business card stand out from others. I have also uploaded each clinician's name and their unique location and phone number.

Our idea is to have one side be black with our logo. Then, on the other side have business cards for each individual. Plus, we want one card that is "generic" with no specific clinician's name listed so that we can give clients an appointment card when they leave. Some clinicians have two locations - we're open to design and background color, but we have started going with branding colors of black, the yellow in the logo files attached, and sometimes a gray. Our new office has been decorated using this theme.

Target Market(s)

individuals and families in need of behavioral health services; potential professional referral sources; existing referral sources

Industry/Entity Type

Business

Contact Information for Business Card

I attached a Word doc that provides clinician names, credentials and location information specific to each individual.

Font styles to use
Serif

Colors
000000
fbed22
dbdbdb
9d9d9d
c3c3c3

Requirements
Must have
• 1) use of the company logo that has been attached; 2) a template that provides us space to individualize business cards for all of our clinicians; 3) should stick to the colors we are branding with: black, yellow from the logo file, maybe a gray shade and we're open to a suggestion on a shade of white.
Nice to have
• Group discussion culminated in the thought that one side would be black with just our logo - no clinician names, etc. A unique design - rounded edges, unique size, some catchy lay-out would be nice.
Should not have
• Must not be too busy. Should look "clean." The project should stick to branding colors: black, yellow (from the logo file), maybe a gray and shade of white.

```html
<!DOCTYPE html>
<html lang="en">
<head>
<meta charset="utf-8">
<title>Meadowlark Counseling Partners – Business Card</title>
<link rel="stylesheet" href="https://fonts.googleapis.com/css2?family=Cormorant+Garamond:wght@500&family=Montserrat:wght@400;600&display=swap">
<style>
  :root {
    --backdrop: #efede8;
    --card-gray: #9d9d9d;
    --card-white: #ffffff;
    --ink: #000000;
    --ink-soft: #222222;
    --on-gray: #ffffff;
    --shadow: rgba(0,0,0,0.28);
  }
  html, body {
    margin: 0;
    padding: 0;
    width: 1200px;
    height: 929px;
    overflow: hidden;
    background: var(--backdrop);
  }
  .canvas {
    position: relative;
    width: 1200px;
    height: 929px;
  }
  .card {
    position: absolute;
    width: 520px;
    height: 297px;
    box-shadow: 0 6px 14px var(--shadow);
  }
  .card--front {
    left: 120px;
    top: 150px;
    background: var(--card-gray);
    display: flex;
    align-items: center;
    justify-content: center;
  }
  .brand-name {
    display: flex;
    align-items: center;
    gap: 14px;
    color: var(--on-gray);
    font-family: "Cormorant Garamond", serif;
    font-weight: 500;
    text-transform: uppercase;
    letter-spacing: 2px;
    text-align: center;
    line-height: 1.15;
    font-size: 24px;
  }
  .brand-mark {
    width: 18px;
    height: 18px;
    border-radius: 50%;
    background: var(--on-gray);
    flex: none;
  }
  .card--back {
    left: 560px;
    top: 480px;
    background: var(--card-white);
  }
  .identity {
    position: absolute;
    left: 74px;
    top: 100px;
    text-align: right;
  }
  .person-name {
    font-family: "Cormorant Garamond", serif;
    font-weight: 500;
    font-size: 26px;
    letter-spacing: 1.5px;
    color: var(--ink);
    text-transform: uppercase;
    margin: 0;
  }
  .person-title {
    font-family: "Montserrat", sans-serif;
    font-weight: 600;
    font-size: 14px;
    color: var(--ink);
    margin: 2px 0 0;
  }
  .divider {
    position: absolute;
    left: 268px;
    top: 86px;
    width: 1px;
    height: 72px;
    background: var(--ink);
  }
  .contact-list {
    position: absolute;
    left: 286px;
    top: 88px;
    margin: 0;
    padding: 0;
    list-style: none;
    font-family: "Montserrat", sans-serif;
    font-size: 13px;
    color: var(--ink-soft);
  }
  .contact-list li {
    display: flex;
    align-items: center;
    gap: 10px;
    height: 22px;
  }
  .contact-list svg { width: 11px; height: 11px; flex: none; }
  .address {
    position: absolute;
    left: 0;
    right: 0;
    bottom: 44px;
    text-align: center;
    font-family: "Montserrat", sans-serif;
    font-size: 13px;
    color: var(--ink-soft);
    margin: 0;
  }
</style>
</head>
<body>
<main class="canvas">
  <section class="card card--front" aria-label="Card front">
    <div class="brand-name">
      <span class="brand-mark"></span>
      <span>Meadowlark<br>Counseling Partners, LLC</span>
    </div>
  </section>

  <section class="card card--back" aria-label="Card back">
    <div class="identity">
      <p class="person-name">Daniel Hart</p>
      <p class="person-title">CEO</p>
    </div>
    <div class="divider"></div>
    <ul class="contact-list">
      <li>
        <svg viewBox="0 0 12 12" aria-hidden="true"><rect x="3" y="0.5" width="6" height="11" rx="1" fill="none" stroke="#000" stroke-width="1"/><line x1="5" y1="9.5" x2="7" y2="9.5" stroke="#000"/></svg>
        000-123-4567
      </li>
      <li>
        <svg viewBox="0 0 12 12" aria-hidden="true"><rect x="3" y="0.5" width="6" height="3" fill="#000"/><rect x="0.5" y="4" width="11" height="5" rx="1" fill="#000"/><rect x="3" y="8" width="6" height="3.5" fill="#000" stroke="#fff" stroke-width="0.6"/></svg>
        000-123-4567
      </li>
      <li>
        <svg viewBox="0 0 12 12" aria-hidden="true"><rect x="0.5" y="2.5" width="11" height="7.5" fill="#000"/><polyline points="0.5,2.5 6,7 11.5,2.5" fill="none" stroke="#fff" stroke-width="0.8"/></svg>
        daniel.hart@meadowlark.com
      </li>
    </ul>
    <p class="address">Prairie Point Centre Topeka</p>
  </section>
</main>
</body>
</html>
```